2023 Cheers to 50 Years Graphic

Hi - I'd like a high-res image that's also print ready that we can use around our office with our 2023 slogan: Cheers to 50 years!

Ideally we'd like a catchy image, the slogan and our logo.

I'll attach the 2022 example. Please use our 50th anniversary logo also attached.

Graphic could be anything celebratory!

Main demographic is males.

Maybe cheers of champagne glasses or beer. But open top option that does not involve alcohol too.

```html
<!DOCTYPE html>
<html lang="en">
<head>
<meta charset="utf-8">
<title>2023 Cheers to 50 Years</title>
<link rel="stylesheet" href="https://fonts.googleapis.com/css2?family=Lobster&display=swap">
<style>
  :root {
    --ink-navy: #2e3a85;
    --spark-white: #fffbe8;
    --spark-gold: #f3cf7a;
    --ember-amber: #b88434;
    --night-teal: #2c4a5a;
    --night-dark: #2a2418;
  }
  html, body {
    margin: 0;
    padding: 0;
    width: 1200px;
    height: 815px;
    overflow: hidden;
    background: var(--night-dark);
  }
  .poster {
    position: relative;
    width: 1200px;
    height: 815px;
    overflow: hidden;
    font-family: "Lobster", cursive;
    color: var(--ink-navy);
  }
  .sparkler-photo {
    position: absolute;
    inset: 0;
    background:
      radial-gradient(ellipse 38% 42% at 53% 54%, var(--spark-white) 0%, rgba(255, 246, 205, 0.9) 35%, rgba(243, 207, 122, 0) 100%),
      radial-gradient(ellipse 75% 80% at 52% 52%, var(--spark-gold) 0%, #e2b55e 45%, var(--ember-amber) 75%, rgba(184, 132, 52, 0) 100%),
      linear-gradient(135deg, var(--night-teal) 0%, #6b6044 35%, #8a6a34 65%, var(--night-dark) 100%);
  }
  .headline {
    position: absolute;
    left: 0;
    margin: 0;
    font-weight: 400;
    line-height: 1;
    white-space: nowrap;
    text-align: center;
  }
  .headline-year {
    top: 150px;
    left: 365px;
    width: 400px;
    font-size: 130px;
  }
  .headline-slogan {
    top: 302px;
    left: 94px;
    width: 1000px;
    font-size: 128px;
  }
  .brand {
    position: absolute;
    left: 858px;
    top: 636px;
    display: flex;
    align-items: center;
    gap: 10px;
    font-size: 28px;
    line-height: 1;
    color: var(--ink-navy);
  }
  .brand-dot {
    width: 22px;
    height: 22px;
    border-radius: 50%;
    background: var(--ink-navy);
  }
</style>
</head>
<body>
  <main class="poster">
    <div class="sparkler-photo" role="img" aria-label="Close-up photograph of a lit sparkler bursting with golden sparks against a dark blue night"></div>
    <h1 class="headline headline-year">2023</h1>
    <p class="headline headline-slogan">Cheers to 50 years!</p>
    <div class="brand">
      <span class="brand-dot"></span>
      <span class="brand-name">Harborline Supply</span>
    </div>
  </main>
</body>
</html>
```